Arborist chip truck vehicle wrap / graphics

We need a wrap design for our chipper truck that we can tie other vehicles in with. We would like to see designs incorporating our logo colors in it and potentially some gold highlights.
Id like it to say Tree ROVER or tree surgeon somewhere.
a modern look is preferable
I would like the final design to be memorable and fairly simple.
Keep in mind this does not have to be a full truck wrap as we do like the white look. were looking for something interesting, use our logo as inspiration, we love it.
were highly trained and skilled and work on high end properties usually.

Target Market(s)

High end homeowners

Font styles to use
Other font styles liked:
• whatever my logo has on it

Requirements
Must have
• logo and name -
• the phrase tree Rover and /or tree surgeon
• some of our colors
• ceritifed arborist logo
• and member oke logo
Nice to have
• maybe something saying " Keeping your trees healthy and happy"
Should not have
• too busy
• there is no back gate so dont worry about the rear of the truck

```html
<!DOCTYPE html>
<html lang="en">
<head>
<meta charset="utf-8">
<title>Larch Tree Company – Tree Surgeon Vehicle Graphic</title>
<link rel="stylesheet" href="https://fonts.googleapis.com/css2?family=Anton&display=swap">
<style>
  :root {
    --green: #0a9444;
    --brown: #5c3816;
    --white: #ffffff;
    --gold: #f2e06a;
    --photo-light: #efe9e2;
    --photo-bark: #8a6a4c;
    --photo-leaf: #7d9a4a;
  }
  html, body {
    margin: 0;
    padding: 0;
    overflow: hidden;
    background: var(--white);
  }
  .wrap-panel {
    position: relative;
    width: 1200px;
    height: 846px;
    overflow: hidden;
    background: var(--white);
    font-family: "Anton", "Arial Narrow", sans-serif;
  }
  .hero-photo {
    position: absolute;
    left: 0;
    top: 0;
    width: 1200px;
    height: 400px;
    background:
      radial-gradient(ellipse 260px 140px at 1010px 130px, rgba(255,255,255,0.95), rgba(255,255,255,0) 100%),
      radial-gradient(ellipse 230px 90px at 190px 70px, rgba(255,255,255,0.9), rgba(255,255,255,0) 100%),
      linear-gradient(180deg, rgba(255,255,255,0) 55%, var(--white) 100%),
      linear-gradient(100deg, var(--photo-leaf) 0%, var(--photo-bark) 25%, var(--photo-light) 45%, var(--photo-bark) 65%, var(--photo-light) 85%, var(--photo-bark) 100%);
  }
  .brand {
    position: absolute;
    left: 64px;
    top: 44px;
    display: flex;
    align-items: center;
    gap: 12px;
    color: var(--green);
    font-size: 34px;
    line-height: 1;
    letter-spacing: 1px;
  }
  .brand-mark {
    width: 52px;
    height: 52px;
    border-radius: 50%;
    background: var(--green);
  }
  .service-title {
    position: absolute;
    left: 850px;
    top: 58px;
    width: 320px;
    margin: 0;
    text-align: center;
    color: var(--green);
    font-size: 77px;
    font-weight: 400;
    line-height: 80px;
    letter-spacing: 1px;
  }
  .tagline {
    position: absolute;
    left: 0;
    top: 476px;
    width: 1200px;
    margin: 0;
    text-align: center;
    font-size: 113px;
    font-weight: 400;
    line-height: 112px;
    letter-spacing: 1px;
  }
  .tagline .green { color: var(--green); }
  .tagline .brown { color: var(--brown); }
  .credentials {
    position: absolute;
    left: 1030px;
    top: 732px;
    display: flex;
    gap: 12px;
  }
  .credential-badge {
    width: 50px;
    height: 84px;
    background: var(--green);
    border: 3px solid var(--gold);
    box-sizing: border-box;
  }
  .credential-badge.member { width: 53px; }
  .accent-band {
    position: absolute;
    left: 0;
    bottom: 0;
  }
</style>
</head>
<body>
  <main class="wrap-panel">
    <div class="hero-photo" role="img" aria-label="Photo of an arborist in a green shirt and climbing harness working high among pine tree branches"></div>

    <div class="brand">
      <span class="brand-mark"></span>
      <span class="brand-name">LARCH TREE COMPANY</span>
    </div>

    <h2 class="service-title">TREE<br>SURGEON</h2>

    <h1 class="tagline">
      <span class="green">KEEPING</span> <span class="brown">YOUR</span> <span class="green">TREES</span><br>
      <span class="brown">HEALTHY</span> <span class="green">AND</span> <span class="brown">HAPPY</span>
    </h1>

    <div class="credentials">
      <div class="credential-badge" aria-label="Certified arborist badge"></div>
      <div class="credential-badge member" aria-label="Association member badge"></div>
    </div>

    <svg class="accent-band" width="340" height="68" viewBox="0 0 340 68" aria-hidden="true">
      <polygon points="0,0 304,0 332,68 0,68" fill="var(--green)"/>
    </svg>
  </main>
</body>
</html>
```